Quillmont Booking Engine Marketing Site

Hi,
I’m currently in the process of putting together a web application with the intention of providing small resorts/B&Bs/small hotels the ability to allow their customers to book online.
I’m looking to have a design created for a marketing site, to give potential customers additional information about my booking engine, as well as to help drive sign-ups. A lot of the competition out there appears outdated, so I would like something that is more modern and up to date.
I am looking for just the design (i’m a web developer, but I lack the creative skills for a good marketing site)
For some more background, I will be targeting business owners of smaller resorts and Bed & Breakfasts. These are typically family owned small businesses that may only have a 10 room setup. These businesses will also typically have additional amenities that they will have to rent out or sell to their clients ( ex. Spa, fruit basket, water sport rentals). My software will provide them with the ability to sell their amenities as well.
I’m open to different designs, but my main thing is I want it to look modern, and I want it to have several callouts to sign up for my product.
I am looking to have the homepage created, 1 interior page, and a style guide created (to show form fields, H1’s, etc.).
I had a logo created a couple months ago that will be included with this project brief.
If you need any additional information feel free to reach out to me.

Target Market(s)

This site will be targeted small business owners who are running small resorts, Bed and Breakfasts, or any business that provides rooms for their clients.

Industry/Entity Type

Saas

Number of Pages Required

2 page

Font styles to use
Sans Serif

Colors

Designer to choose colors to be used in the design.

Requirements
Must have
• A modern feel, with several CTA's that will drive to the registration page on the homepage. on the internal page, I mostly just need the page layout, I will reuse that page layout. and a style guide if at all possible (include colors, form fields, H1's, etc.)
Nice to have
• maybe a hero image at the top with buttons over the top? again i'm pretty open to most anything.
Should not have
• I like images, but I don't want the page overrun with images. A good balance.

```html
<!DOCTYPE html>
<html lang="en">
<head>
<meta charset="utf-8">
<title>Quillmont Booking Engine – Online booking for small resorts and B&amp;Bs</title>
<link href="https://fonts.googleapis.com/css2?family=Lato:wght@400;700;900&display=swap" rel="stylesheet">
<style>
:root{
  --green:#7ab51d;
  --green-dark:#5f9212;
  --navy:#1b3556;
  --ink:#222;
  --text:#444;
  --muted:#777;
  --light:#f4f4f4;
  --dark:#23272e;
  --news:#0f1c2e;
  --footer:#1f2329;
  --white:#fff;
}
*{box-sizing:border-box;margin:0;padding:0}
html,body{width:1200px;height:3103px;overflow:hidden}
body{font-family:'Lato',sans-serif;color:var(--text);background:var(--white);position:relative}
section,header,footer{position:absolute;left:0;width:1200px}

/* header */
.site-header{top:0;height:80px;background:var(--white);box-shadow:0 1px 4px rgba(0,0,0,.08);z-index:2}
.brand{position:absolute;left:215px;top:18px;display:flex;align-items:center;gap:10px}
.brand-dot{width:40px;height:40px;border-radius:50%;background:var(--green)}
.brand-name{color:var(--navy);font-weight:700;font-size:17px;line-height:19px;letter-spacing:.5px}
.nav{position:absolute;right:215px;top:34px;display:flex;align-items:center;font-size:13px}
.nav a{color:var(--ink);text-decoration:none;padding:0 14px;border-right:1px solid #ccc;line-height:14px}
.nav a.active{color:var(--green)}
.nav .search{padding-left:14px;display:flex}

/* hero */
.hero{top:80px;height:600px;overflow:hidden}
.hero-photo{position:absolute;inset:0;background:linear-gradient(180deg,#2d3b46 0%,#3e4c56 45%,#1f2a31 100%)}
.hero-content{position:absolute;left:0;right:0;top:105px;text-align:center}
.hero-mark{width:62px;height:62px;border-radius:50%;background:var(--green);margin:0 auto 40px}
.hero-title{font-size:44px;font-weight:700;color:var(--white);letter-spacing:-.5px;line-height:52px}
.hero-sub{font-size:19px;color:var(--white);margin-top:4px}
.search-bar{position:absolute;left:283px;top:393px;width:634px;height:48px;background:#111;border-radius:3px;padding:5px;display:flex;gap:8px}
.search-field{flex:1;background:var(--white);display:flex;align-items:center;font-size:13px}
.search-select{width:116px;padding-left:14px;color:var(--ink);border-right:1px solid #ddd;height:24px;display:flex;align-items:center;gap:10px}
.search-input{padding-left:16px;color:#999}
.search-btn{width:138px;background:var(--green);color:var(--white);font-weight:700;font-size:17px;display:flex;align-items:center;justify-content:center}
.scroll-arrow{position:absolute;left:587px;top:540px}

/* section title */
.section-title{font-size:15px;font-weight:400;letter-spacing:2.5px;color:var(--ink);text-align:center}
.title-rule{width:78px;height:3px;margin:12px auto 0;background:linear-gradient(90deg,var(--green) 50%,var(--navy) 50%)}
.dark .section-title{color:var(--white)}

/* partners */
.partners{top:680px;height:198px;background:var(--light);padding-top:40px}
.partner-row{position:absolute;top:118px;left:150px;width:900px;display:flex;align-items:center;justify-content:space-between}
.partner{font-size:26px;font-weight:700;color:#4a4f57;letter-spacing:-.5px}

/* about */
.about{top:878px;height:452px;padding-top:34px}
.cards{position:absolute;left:215px;top:100px;display:flex;gap:23px}
.card{width:242px}
.card-box{height:177px;background:var(--light);display:flex;flex-direction:column;align-items:center;justify-content:flex-end;padding-bottom:24px}
.card-box svg{margin-bottom:30px}
.card-label{font-size:12px;color:var(--ink)}
.card-text{font-size:12px;line-height:19px;color:var(--text);padding:12px 10px 0;text-align:justify;height:107px}
.card-more{display:flex;justify-content:space-between;margin-top:8px}
.read-more{display:inline-flex;align-items:center;gap:8px;height:20px;padding:0 18px 0 6px;background:var(--green);color:var(--ink);font-size:10px;font-weight:700;clip-path:polygon(0 0,100% 0,92% 100%,0 100%)}

/* video */
.video{top:1330px;height:437px;overflow:hidden;padding-top:36px}
.video-bg{position:absolute;inset:0;background:linear-gradient(100deg,#2b3037 0%,#363c44 60%,#2a2e34 100%)}
.video .section-title,.video .title-rule{position:relative}
.video-copy{position:absolute;left:215px;top:100px;width:340px;color:var(--white)}
.video-copy h2{font-size:30px;font-weight:700;letter-spacing:.5px;margin-bottom:16px}
.video-copy p{font-size:12px;line-height:17px;margin-bottom:12px}
.outline-btn{display:inline-block;margin-top:40px;border:1px solid var(--white);border-radius:14px;padding:6px 22px;font-size:12px;color:var(--white)}
.video-frame{position:absolute;left:592px;top:108px;width:393px;height:289px;border:2px solid #ddd;padding:12px}
.video-still{width:100%;height:100%;background:linear-gradient(160deg,#8fcc24,#6ea81a);display:flex;align-items:center;justify-content:center}

/* projects */
.projects{top:1767px;height:1058px;overflow:hidden}
.project-bg{position:absolute;left:0;top:0}
.projects .section-title{position:absolute;top:36px;left:0;right:0}
.project{position:absolute;left:0;width:1200px}
.project-photo{position:absolute;width:445px;height:250px;background:linear-gradient(90deg,#e6e4e0 0%,#f1f0ed 60%,#dcdad6 100%);box-shadow:0 6px 16px rgba(0,0,0,.22)}
.project-copy{position:absolute;width:330px}
.project-copy h3{font-size:15px;font-weight:700;color:var(--ink);margin-bottom:20px}
.project-copy p{font-size:11px;line-height:17px;color:var(--text);margin-bottom:14px}
.ticks{list-style:none;font-size:11px;line-height:21px;color:var(--text);margin-bottom:22px}
.ticks li{padding-left:30px;position:relative}
.ticks li::before{content:"";position:absolute;left:2px;top:8px;width:6px;height:6px;border-radius:50%;background:var(--ink)}

/* newsletter */
.newsletter{top:2825px;height:80px;background:var(--news);display:flex;align-items:center}
.newsletter-label{position:absolute;left:292px;font-size:16px;color:var(--white);letter-spacing:.4px}
.newsletter-form{position:absolute;left:656px;display:flex;height:22px}
.newsletter-email{width:202px;background:var(--white);font-size:11px;color:#666;padding:4px 8px}
.newsletter-send{width:54px;background:var(--green);color:var(--ink);font-size:11px;font-weight:700;display:flex;align-items:center;justify-content:center}

/* footer */
.site-footer{top:2905px;height:198px;background:var(--footer);color:var(--white)}
.footer-brand{position:absolute;left:215px;top:40px;display:flex;align-items:center;gap:10px}
.footer-brand .brand-name{color:var(--green);font-size:22px;line-height:24px}
.footer-brand .brand-dot{width:44px;height:44px}
.apps{position:absolute;left:528px;top:35px;font-size:11px}
.app-badges{display:flex;gap:14px;margin-top:22px}
.app-badge{width:76px;height:24px;border-radius:4px;background:#000;border:1px solid #888}
.contact{position:absolute;right:215px;top:35px;text-align:right;font-size:11px;line-height:13px;font-weight:700;font-style:normal}
.footer-rule{position:absolute;left:120px;right:120px;top:145px;height:1px;background:#444}
.social{position:absolute;left:224px;top:168px;display:flex;gap:16px}
.social span{width:10px;height:10px;border-radius:50%;background:var(--green)}
.copyright{position:absolute;left:0;right:0;top:166px;text-align:center;font-size:10px;color:#aaa}
</style>
</head>
<body>

<header class="site-header">
  <div class="brand"><span class="brand-dot"></span><span class="brand-name">QUILLMONT<br>BOOKING ENGINE</span></div>
  <nav class="nav">
    <a class="active">Home</a><a>About</a><a>Features</a><a>Pricing</a><a>FAQ</a><a>Contact</a>
    <span class="search"><svg width="12" height="12" viewBox="0 0 12 12"><circle cx="5" cy="5" r="3.8" fill="none" stroke="#222" stroke-width="1.4"/><line x1="8" y1="8" x2="11" y2="11" stroke="#222" stroke-width="1.6"/></svg></span>
  </nav>
</header>

<section class="hero">
  <div class="hero-photo" role="img" aria-label="Misty city street with tall buildings, street lamps and a pedestrian"></div>
  <div class="hero-content">
    <div class="hero-mark"></div>
    <h1 class="hero-title">QUILLMONT BOOKING ENGINE</h1>
    <p class="hero-sub">Online booking for small resorts, B&amp;Bs and hotels</p>
  </div>
  <div class="search-bar">
    <div class="search-field">
      <div class="search-select">Bed &amp; Breakfast <svg width="7" height="5" viewBox="0 0 7 5"><path d="M0 0h7L3.5 5z" fill="#222"/></svg></div>
      <div class="search-input">Enter your business email address</div>
    </div>
    <div class="search-btn">Sign Up Free</div>
  </div>
  <svg class="scroll-arrow" width="26" height="36" viewBox="0 0 26 36"><path d="M13 0v34M2 23l11 11 11-11" fill="none" stroke="#fff" stroke-width="2"/></svg>
</section>

<section class="partners">
  <h2 class="section-title">OUR PARTNERS</h2>
  <div class="title-rule"></div>
  <div class="partner-row">
    <svg width="26" height="14" viewBox="0 0 26 14"><path d="M25 7H2M8 1L2 7l6 6" fill="none" stroke="#333" stroke-width="1.6"/></svg>
    <span class="partner">Cashvale</span>
    <span class="partner">Netmoor</span>
    <span class="partner">Paybrook</span>
    <span class="partner">Payridge</span>
    <span class="partner">Payloft</span>
    <svg width="26" height="14" viewBox="0 0 26 14"><path d="M1 7h23M18 1l6 6-6 6" fill="none" stroke="#333" stroke-width="1.6"/></svg>
  </div>
</section>

<section class="about">
  <h2 class="section-title">ABOUT</h2>
  <div class="title-rule"></div>
  <div class="cards">
    <article class="card">
      <div class="card-box">
        <svg width="70" height="56" viewBox="0 0 70 56"><path d="M14 20a10 10 0 0 1 20 0c0 8-10 20-10 20S14 28 14 20z" fill="none" stroke="#333" stroke-width="2.5"/><circle cx="24" cy="20" r="3.5" fill="#e0533a"/><path d="M46 10a6 6 0 0 1 12 0c0 5-6 12-6 12s-6-7-6-12z" fill="#333"/><path d="M52 26v6M50 38l-6 6M38 48h-8" stroke="#333" stroke-width="2.5" stroke-dasharray="3 4" fill="none"/></svg>
        <span class="card-label">Get Found Online</span>
      </div>
      <p class="card-text">Guests find your rooms and book them straight from your own website, any time of day. No middlemen and no phone tag, just a clear calendar that fills itself.</p>
      <div class="card-more"><span class="read-more">Sign Up <svg width="16" height="8" viewBox="0 0 16 8"><path d="M0 4h14M11 1l3 3-3 3" fill="none" stroke="#222" stroke-width="1.2"/></svg></span></div>
    </article>
    <article class="card">
      <div class="card-box">
        <svg width="76" height="52" viewBox="0 0 76 52"><rect x="6" y="8" width="64" height="32" rx="8" fill="#fff" stroke="#333" stroke-width="2.5"/><rect x="6" y="26" width="64" height="8" fill="#9bcf2f"/><rect x="14" y="14" width="12" height="9" fill="#333"/><rect x="32" y="14" width="12" height="9" fill="#333"/><rect x="50" y="14" width="12" height="9" fill="#333"/><circle cx="20" cy="42" r="6" fill="#333"/><circle cx="56" cy="42" r="6" fill="#333"/></svg>
        <span class="card-label">Sell Your Amenities</span>
      </div>
      <p class="card-text">Offer spa visits, fruit baskets and water sport rentals right inside the booking. Guests add extras in one click and you earn more from every single stay.</p>
      <div class="card-more"><span></span><span class="read-more">Sign Up <svg width="16" height="8" viewBox="0 0 16 8"><path d="M0 4h14M11 1l3 3-3 3" fill="none" stroke="#222" stroke-width="1.2"/></svg></span><span></span></div>
    </article>
    <article class="card">
      <div class="card-box">
        <svg width="44" height="60" viewBox="0 0 44 60"><circle cx="22" cy="18" r="16" fill="#333"/><text x="22" y="25" font-family="Lato,sans-serif" font-size="20" font-weight="700" fill="#fff" text-anchor="middle">$</text><path d="M22 34v22M22 48c-6-8-14-6-16-4 4 4 10 6 16 4zM22 48c6-8 14-6 16-4-4 4-10 6-16 4z" fill="#333" stroke="#333" stroke-width="2"/></svg>
        <span class="card-label">Save Money</span>
      </div>
      <p class="card-text">One fair monthly price built for family-run places with ten rooms or fewer. No setup fees, no commission on bookings and no contract to tie you down.</p>
      <div class="card-more"><span></span><span class="read-more">Sign Up <svg width="16" height="8" viewBox="0 0 16 8"><path d="M0 4h14M11 1l3 3-3 3" fill="none" stroke="#222" stroke-width="1.2"/></svg></span></div>
    </article>
  </div>
</section>

<section class="video dark">
  <div class="video-bg" role="img" aria-label="Dim photo of a traveller looking out over a city"></div>
  <h2 class="section-title">WATCH VIDEO</h2>
  <div class="title-rule"></div>
  <div class="video-copy">
    <h2>SEE HOW IT WORKS</h2>
    <p>Take a two-minute tour of the booking engine and see how easy it is to put your rooms online.</p>
    <p>Set it up in an afternoon, no developer needed.</p>
    <p>Watch a guest choose a room, add a spa visit and pay, all from your own site.</p>
    <span class="outline-btn">Watch Video</span>
  </div>
  <div class="video-frame">
    <div class="video-still" role="img" aria-label="Video still of a domed cathedral and a bridge with walkers, tinted green">
      <svg width="38" height="38" viewBox="0 0 38 38"><circle cx="19" cy="19" r="18" fill="#fff"/><path d="M15 11l12 8-12 8z" fill="#7ab51d"/></svg>
    </div>
  </div>
</section>

<section class="projects">
  <svg class="project-bg" width="1200" height="1058" viewBox="0 0 1200 1058">
    <rect width="1200" height="1058" fill="#f7f8fa"/>
    <polygon points="0,0 352,0 600,401 0,401" fill="#7ab51d"/>
    <rect x="0" y="401" width="1200" height="327" fill="#ffffff"/>
    <polygon points="848,401 1200,401 1200,728 600,728" fill="#7ab51d"/>
    <polygon points="0,728 352,728 600,1058 0,1058" fill="#7ab51d"/>
  </svg>
  <h2 class="section-title">FEATURES</h2>

  <div class="project" style="top:0">
    <div class="project-photo" style="left:92px;top:109px" role="img" aria-label="Desk with a computer monitor, a potted plant and a yellow mug"></div>
    <div class="project-copy" style="left:664px;top:108px">
      <h3>TAKE BOOKINGS AROUND THE CLOCK.</h3>
      <p>Add a booking form to your website in minutes. Guests see live room availability and book instantly, even while you sleep.</p>
      <ul class="ticks"><li>Live room calendar.</li><li>Instant email confirmations.</li><li>Works on phones and tablets.</li><li>Matches your website colours.</li></ul>
      <span class="read-more">Sign Up Free <svg width="16" height="8" viewBox="0 0 16 8"><path d="M0 4h14M11 1l3 3-3 3" fill="none" stroke="#222" stroke-width="1.2"/></svg></span>
    </div>
  </div>

  <div class="project" style="top:401px">
    <div class="project-copy" style="left:215px;top:40px">
      <h3>SELL EXTRAS WITH EVERY STAY.</h3>
      <p>List your amenities next to your rooms. Spa treatments, fruit baskets and boat rentals can be added by guests during checkout.</p>
      <ul class="ticks"><li>Unlimited add-on items.</li><li>Set prices per day or per item.</li><li>Track stock and rentals.</li><li>One payment for everything.</li></ul>
      <span class="read-more">Sign Up Free <svg width="16" height="8" viewBox="0 0 16 8"><path d="M0 4h14M11 1l3 3-3 3" fill="none" stroke="#222" stroke-width="1.2"/></svg></span>
    </div>
    <div class="project-photo" style="left:663px;top:40px" role="img" aria-label="Desk with a computer monitor, a potted plant and a yellow mug"></div>
  </div>

  <div class="project" style="top:728px">
    <div class="project-photo" style="left:92px;top:38px" role="img" aria-label="Desk with a computer monitor, a potted plant and a yellow mug"></div>
    <div class="project-copy" style="left:664px;top:40px">
      <h3>MANAGE IT ALL IN ONE PLACE.</h3>
      <p>A simple dashboard for small teams. See arrivals, payments and amenity orders at a glance, without any training.</p>
      <ul class="ticks"><li>Daily arrivals list.</li><li>Secure online payments.</li><li>Guest history and notes.</li><li>Friendly support by email.</li></ul>
      <span class="read-more">Sign Up Free <svg width="16" height="8" viewBox="0 0 16 8"><path d="M0 4h14M11 1l3 3-3 3" fill="none" stroke="#222" stroke-width="1.2"/></svg></span>
    </div>
  </div>
</section>

<section class="newsletter">
  <span class="newsletter-label">Start your free trial today</span>
  <div class="newsletter-form"><span class="newsletter-email">Email</span><span class="newsletter-send">Sign Up</span></div>
</section>

<footer class="site-footer">
  <div class="footer-brand"><span class="brand-dot"></span><span class="brand-name">QUILLMONT<br>BOOKING ENGINE</span></div>
  <div class="apps">Available on
    <div class="app-badges"><span class="app-badge"></span><span class="app-badge"></span></div>
  </div>
  <address class="contact">(+000) 555. 0142. 310<br>Your Company Address<br>Your City<br>info@quillmonteng.com<br>www.quillmonteng.com</address>
  <div class="footer-rule"></div>
  <div class="social"><span></span><span></span><span></span><span></span><span></span><span></span></div>
  <p class="copyright">© 2018 QUILLMONT BOOKING ENGINE &nbsp;-&nbsp; All Rights Reserved</p>
</footer>

</body>
</html>
```